Webdesign für Elektroplanungsbüro
Zielgruppe
Das Elektroplanungsbüro Brambeck besteht seit mehreren Jahren. Die Planungen umfassen deutschlandweit Anlagen im Industriebau, Wohn- und Gewerbebereich als Neubauten, sowie als Sanierungen/ Modernisierungen/ Umbaumaßnahmen, auch denkmalgeschützter Gebäude sowie musealer- und sakraler Gebäude.
Die Auftraggeber kommen vorwiegend aus dem öffentlichen Bereich (Stadtverwaltungen/ Tiefbauämter/ Staatsbetriebe des Velmarischen Grundstücks- und Bauverwaltung/ Hochbauämter/ Gemeinnützige Institutionen)
Aufgabenstellung
Die webseiten von www.orvatek-plan.de und von www.qumsa.de gefallen (großes headerbild, moderne Navigation)
Wir bevorzugen Photoshop

```html
<!DOCTYPE html>
<html lang="de">
<head>
<meta charset="utf-8">
<title>Elektroplanung Brambeck</title>
<link href="https://fonts.googleapis.com/css2?family=Poppins:ital,wght@0,400;0,500;0,600;1,400&display=swap" rel="stylesheet">
<style>
:root{
  --green:#6e9d2b;
  --navy:#1c2340;
  --text:#2a2a2a;
  --grey-band:#e9e9e9;
  --line:#c9c9c9;
  --white:#fff;
}
*{margin:0;padding:0;box-sizing:border-box}
html,body{width:1200px;height:2264px;overflow:hidden}
body{position:relative;background:var(--white);font-family:'Poppins',sans-serif;color:var(--text)}
.abs{position:absolute}
a{color:inherit;text-decoration:none}

/* header */
.site-header{left:0;top:0;width:1200px;height:70px;background:var(--white)}
.brand{left:142px;top:24px;display:flex;align-items:center;gap:8px;font-weight:600;font-size:15px;color:var(--green);letter-spacing:.5px}
.brand-dot{width:12px;height:12px;border-radius:50%;background:var(--green)}
.main-nav{right:140px;top:29px;display:flex;gap:26px;font-size:11px;font-weight:500;color:var(--navy)}

/* hero */
.hero{left:0;top:70px;width:1200px;height:573px;background:linear-gradient(100deg,#5d5f63 0%,#8a8b8d 35%,#4a3f36 60%,#c58a45 78%,#3b2f27 100%)}
.hero-text{left:201px;top:258px;color:var(--white)}
.hero-text .kicker{font-size:16px;margin-bottom:12px}
.hero-text h1{font-size:35px;font-weight:600;line-height:44px;width:460px}

/* services */
.section-title{font-size:15px;font-weight:500;letter-spacing:2.4px;color:var(--green);text-transform:uppercase}
.services-title{left:142px;top:697px}
.services-intro{left:144px;top:730px;width:460px;font-size:9.5px;line-height:15px}
.service-grid{left:142px;top:776px;width:464px;display:grid;grid-template-columns:218px 218px;column-gap:28px}
.service{height:45px;border-bottom:1.5px solid var(--green);display:flex;align-items:center;gap:8px;font-size:10.5px;padding-left:6px}
.service svg{width:28px;height:28px;flex:none}
.more-link{left:520px;top:933px;font-size:10.5px;color:var(--green);display:flex;align-items:center;gap:5px}
.more-link span.dot{width:10px;height:10px;border-radius:50%;background:var(--green);color:#fff;font-size:9px;line-height:10px;text-align:center}
.bolt{left:750px;top:605px}

/* projects */
.projects{left:0;top:1003px;width:1200px;height:250px;background:var(--grey-band)}
.projects-title{left:0;width:1200px;top:62px;text-align:center}
.project-name{left:0;width:1200px;top:107px;text-align:center;font-size:11.5px;font-weight:600;color:var(--navy)}
.project-city{left:0;width:1200px;top:128px;text-align:center;font-size:10.5px}
.btn{background:var(--green);color:var(--white);font-size:10.5px;display:flex;align-items:center;justify-content:center}
.project-btn{left:542px;top:158px;width:121px;height:40px}
.arrow{top:90px}

/* certificates */
.cert-title{left:143px;top:1344px}
.cert-text{left:144px;top:1390px;width:380px;font-size:10.5px;line-height:20px}
.cert-btn{left:143px;top:1458px;width:121px;height:41px}
.cert-doc{top:1568px;width:139px;height:195px;background:#a7aaab;padding:7px}
.cert-doc .paper{width:100%;height:100%;background:#f7f7f5}
.photo-plan{left:718px;top:1321px;width:345px;height:492px;background:linear-gradient(160deg,#cfd3d4,#e7e8e6 50%,#a8a39b)}
.divider{left:113px;top:1871px;width:1002px;height:1px;background:#e1e1e1}

/* contact */
.contact-title{left:0;width:1200px;top:1913px;text-align:center}
.contact-q{left:0;width:1200px;top:1955px;text-align:center;font-size:12px;font-weight:600;color:var(--navy)}
.contact-a{left:0;width:1200px;top:1974px;text-align:center;font-size:11.5px;font-style:italic;color:var(--green)}

/* footer */
.site-footer{left:0;top:2050px;width:1200px;height:214px;background:var(--grey-band)}
.footer-name{left:146px;top:42px;font-size:10px;font-weight:600;letter-spacing:.8px}
.footer-contact{left:145px;top:62px;font-size:9px;letter-spacing:.6px;line-height:14px}
.footer-contact li{list-style:none;display:flex;align-items:center;gap:8px}
.footer-contact svg{width:9px;height:9px}
.footer-contact .mail{color:var(--green)}
.badges{left:641px;top:56px;display:flex;gap:12px;align-items:center}
.badge-circle{width:38px;height:38px;border-radius:50%;background:#fff;border:2px solid #555}
.badge-rect{width:140px;height:38px;background:#fff;border:1px solid #ccc}
.badge-wide{width:100px;height:32px;background:#fff;border:1px solid #ccc}
.footer-rule{left:0;top:135px;width:1200px;height:1px;background:#d6d6d6}
.footer-nav{left:145px;top:156px;display:flex;gap:20px;font-size:10px}
.copyright{left:144px;top:181px;font-size:6.5px;font-weight:500}
</style>
</head>
<body>

<header class="site-header abs">
  <div class="brand abs"><span class="brand-dot"></span>Elektroplanung Brambeck</div>
  <nav class="main-nav abs">
    <a>Leistungen</a><a>Aktuelle Projekte</a><a>Unternehmen</a><a>Karriere</a><a>Downloads</a><a>Engagement</a><a>Kontakt</a>
  </nav>
</header>

<section class="hero abs" role="img" aria-label="Foto einer leuchtenden Glühbirne in einem Innenraum"></section>
<div class="hero-text abs">
  <p class="kicker">A</p>
  <h1>Wir beraten sie, planen und überwachen ihre elektrotechischen anlagen.</h1>
</div>

<section class="services">
  <h2 class="section-title services-title abs">Unser Leistungsspektrum beinhaltet:</h2>
  <p class="services-intro abs">Lorem ipsum dolor sit amet, consectetur adipiscing elit, sed do eiusmod tempor incididunt ut labore et dolore magna aliqua.</p>
  <div class="service-grid abs">
    <div class="service"><svg viewBox="0 0 28 28"><rect x="3" y="3" width="22" height="22" rx="2" fill="none" stroke="#444" stroke-width="1.6"/><path d="M15 6l-5 9h5l-2 8 6-11h-5z" fill="#444"/></svg>Starkstromanlagen</div>
    <div class="service"><svg viewBox="0 0 28 28"><path d="M4 14L14 5l10 9v10H4z" fill="none" stroke="#444" stroke-width="1.6"/><path d="M15 12l-4 6h3l-1 4 4-6h-3z" fill="#444"/></svg>Gebäudeautomation</div>
    <div class="service"><svg viewBox="0 0 28 28"><circle cx="10" cy="14" r="7" fill="none" stroke="#444" stroke-width="1.6"/><path d="M17 8h7M17 14h8M17 20h7" stroke="#444" stroke-width="1.6"/></svg>Informationstechnische Anlagen</div>
    <div class="service"><svg viewBox="0 0 28 28"><rect x="5" y="6" width="18" height="9" fill="none" stroke="#444" stroke-width="1.6"/><circle cx="8" cy="21" r="2.2" fill="#444"/><circle cx="14" cy="21" r="2.2" fill="#444"/><circle cx="20" cy="21" r="2.2" fill="#444"/></svg>Fördertechnische Anlagen</div>
    <div class="service"><svg viewBox="0 0 28 28"><circle cx="14" cy="14" r="11" fill="none" stroke="#444" stroke-width="1.6"/><circle cx="14" cy="14" r="6" fill="#444"/><path d="M15 10l-3 4h2l-1 4 3-5h-2z" fill="#fff"/></svg>Regenerative Anlagen</div>
    <div class="service"><svg viewBox="0 0 28 28"><path d="M14 3a8 8 0 0 0-5 14v4h10v-4a8 8 0 0 0-5-14z" fill="none" stroke="#444" stroke-width="1.6"/><path d="M10 24h8" stroke="#444" stroke-width="1.6"/></svg>Energiemanagement</div>
  </div>
  <a class="more-link abs"><span class="dot">+</span>mehr erfahren</a>
  <svg class="bolt abs" width="310" height="372" viewBox="750 605 310 372">
    <defs><linearGradient id="cityTones" x1="0" y1="0" x2="0" y2="1"><stop offset="0" stop-color="#3e5d86"/><stop offset=".45" stop-color="#b7a782"/><stop offset="1" stop-color="#3d4a2c"/></linearGradient></defs>
    <g fill="none" stroke="#d2d2d2" stroke-width="2">
      <path d="M778 715v-30h30M980 685h30v30M778 890v30h30M980 920h30v-30"/>
    </g>
    <polygon points="895,608 756,826 895,826 895,975 1043,757 895,757" fill="url(#cityTones)" role="img" aria-label="Foto eines beleuchteten Bürogebäudes in der Dämmerung"/>
  </svg>
</section>

<section class="projects abs">
  <svg class="abs" style="left:587px;top:0" width="26" height="14"><polygon points="0,0 26,0 13,14" fill="#fff"/></svg>
  <h2 class="section-title projects-title abs">Aktuelle Projekte</h2>
  <svg class="arrow abs" style="left:146px" width="22" height="52"><path d="M20 2L2 26l18 24" fill="none" stroke="#555" stroke-width="1.2"/></svg>
  <svg class="arrow abs" style="left:1038px" width="22" height="52"><path d="M2 2l18 24L2 50" fill="none" stroke="var(--green)" stroke-width="1.2"/></svg>
  <p class="project-name abs">MUSEUM "WEBEREIZENTRUM ALTES TUCHHAUS AM MÜHLGRABEN"</p>
  <p class="project-city abs">- Talstadt -</p>
  <a class="btn project-btn abs">zu den details</a>
</section>

<section class="certificates">
  <h2 class="section-title cert-title abs">Zertifikate</h2>
  <p class="cert-text abs">Lorem ipsum dolor sit amet, consectetur adipiscing elit, sed do eiusmod tempor incididunt ut labore et dolore magna aliqua. Ut enim ad minim veniam, quis nostrud exercitation ullamco laboris nisi ut aliquip ex ea</p>
  <a class="btn cert-btn abs">Downloads</a>
  <div class="cert-doc abs" style="left:143px"><div class="paper" role="img" aria-label="Urkunde Beratender Ingenieur"></div></div>
  <div class="cert-doc abs" style="left:298px"><div class="paper" role="img" aria-label="Zertifikat Qualitätsmanagement"></div></div>
  <div class="cert-doc abs" style="left:453px"><div class="paper" role="img" aria-label="Zertifikat Fachfirma für Brandmeldeanlagen"></div></div>
  <div class="photo-plan abs" role="img" aria-label="Foto: Hände arbeiten mit Geodreieck und Taschenrechner an einem Bauplan"></div>
</section>

<div class="divider abs"></div>

<section class="contact">
  <h2 class="section-title contact-title abs">Kontakt</h2>
  <p class="contact-q abs">Sie haben Fragen oder wünschen einen Termin?</p>
  <p class="contact-a abs">Wir freuen uns auf Ihren Anruf oder E-Mail. ➞</p>
</section>

<footer class="site-footer abs">
  <p class="footer-name abs">Elektroplanung Brambeck</p>
  <ul class="footer-contact abs">
    <li><svg viewBox="0 0 10 10"><path d="M5 0a3.5 3.5 0 0 0-3.5 3.5C1.5 6 5 10 5 10s3.5-4 3.5-6.5A3.5 3.5 0 0 0 5 0z" fill="#555"/><circle cx="5" cy="3.5" r="1.2" fill="#e9e9e9"/></svg>Lindenhofweg 12, 04815 Talstadt</li>
    <li><svg viewBox="0 0 10 10"><path d="M2 0l2 2.5-1 1.5c.8 1.5 1.5 2.2 3 3l1.5-1L10 8l-1.5 2C4 10 0 6 0 1.5z" fill="#555"/></svg>0341 908172 0</li>
    <li><svg viewBox="0 0 10 10"><rect x="1" y="3" width="8" height="6" fill="#555"/><rect x="3" y="0" width="4" height="3" fill="#555"/></svg>0341 908172 29</li>
    <li><svg viewBox="0 0 10 10"><rect x="0" y="2" width="10" height="7" fill="#555"/><path d="M0 2l5 4 5-4" stroke="#e9e9e9" fill="none"/></svg><span class="mail">info@elektroplanung-brambeck.de</span></li>
  </ul>
  <div class="badges abs">
    <div class="badge-circle"></div><div class="badge-circle"></div><div class="badge-circle"></div><div class="badge-rect"></div><div class="badge-wide"></div>
  </div>
  <div class="footer-rule abs"></div>
  <nav class="footer-nav abs"><a>Home</a><a>Leistungen</a><a>Aktuelle Projekte</a><a>Unternehmen</a><a>Karriere</a><a>Downloads</a><a>Engagement</a><a>Kontakt</a></nav>
  <p class="copyright abs">Copyright © 2022 www.elektroplanung-brambeck.de. Alle Rechte vorbehalten.</p>
</footer>

</body>
</html>
```